Stationery Design Project - Professional Training Company

Full set of statinery in PDF and format that can be given to the printers

Letterhead
Business cards x 3
Compliments slip
Envelope
Updates

Many thanks for all your contributions, the quality of the designs is amazing.

Thank you all so much for your contribution to this project, I am very impressed with the designs and choice of designs, you are all clearly very talented individuals.

I hope to be making a decision on the final choice this evening UAE time.

Best regards and again thank you so much

Gordon

I would like to take this opportunity to thank you all for your contributions, I have been very impressed with each of the designs submitted.

I will shortly go back and give each of you a personal rating on each of your designs.

Again thank you all so much for your efforts

Best Regards

Gordon

Target Market(s)

We are a training company that provides IT training for Medical and Professional Staff, we train professional adults

Industry/Entity Type

Business

Requirements
Must have
• The letterhead and compliments slip must have at the bottom of the page:-

Bright Ledger Pathways LLP operates as a limited liability partnership registered in England and Wales (with registered number OC702614)

Business Cards are to be made up for three people (details of those to be provided after appoval of design but are included in this project) and should contain:

Name
Title
Telephone
email
Address: P.O. Box 418263 Dubai UAE
web address: www.brightledgerpathways.example
Nice to have
• Very clean and professional looking
Should not have
• No look to busy or ovr crowded

```html
<!DOCTYPE html>
<html lang="en">
<head>
<meta charset="utf-8">
<title>Bright Ledger Pathways – Stationery Set</title>
<link href="https://fonts.googleapis.com/css2?family=Open+Sans:wght@400;600;700&display=swap" rel="stylesheet">
<style>
  :root{
    --bg:#efefef;
    --paper:#ffffff;
    --plum:#8a2a7c;
    --plum-dark:#5e1a55;
    --plum-light:#a4458f;
    --green:#4f9b2b;
    --ink:#333333;
    --muted:#8a8a8a;
  }
  *{box-sizing:border-box;margin:0;padding:0}
  html,body{width:1200px;height:1000px;overflow:hidden}
  body{background:var(--bg);font-family:"Open Sans",Arial,sans-serif;color:var(--ink);position:relative}
  .piece{position:absolute;background:var(--paper);overflow:hidden;box-shadow:0 1px 3px rgba(0,0,0,.12)}

  .brand{display:flex;align-items:center;gap:5px;color:var(--plum-dark);font-weight:600;line-height:1.05}
  .brand-dot{border-radius:50%;background:var(--plum);flex:none}
  .split-bar{position:absolute;left:0;right:0;bottom:0;height:4px;display:flex}
  .split-bar span:first-child{flex:1;background:var(--green)}
  .split-bar span:last-child{flex:1;background:var(--plum)}
  .purple-art{background:linear-gradient(135deg,var(--plum-dark) 0%,var(--plum) 45%,var(--plum-light) 70%,var(--plum) 100%)}

  /* Shared document footer */
  .doc-footer{position:absolute;display:flex;align-items:flex-start;gap:8px;font-size:4.2px;color:#666;line-height:1.45}
  .doc-footer .col{padding-right:8px;border-right:0.5px solid #bbb;white-space:nowrap;flex:none}
  .doc-footer .col.legal{border:none;padding-right:0;white-space:normal;flex:1;color:#888}
  .doc-footer b{color:var(--plum);font-weight:600}

  /* Letterhead */
  .letterhead{left:293px;top:127px;width:292px;height:387px}
  .letterhead .brand{position:absolute;left:20px;top:8px;font-size:10px}
  .letterhead .brand-dot{width:14px;height:14px}
  .letterhead .web{position:absolute;right:24px;top:10px;font-size:4.5px;color:var(--muted)}
  .letter-body{position:absolute;left:20px;top:117px;width:250px;font-size:4.6px;line-height:1.6;color:#555}
  .letter-body .salutation{font-size:6px;font-weight:600;color:var(--ink);margin-bottom:10px}
  .letter-body p{margin-bottom:7px;text-align:justify}
  .signoff{position:absolute;right:22px;top:292px;text-align:right;font-size:4.8px;color:#555}
  .signature{width:70px;height:24px;margin:2px 0 2px auto;background:linear-gradient(90deg,rgba(70,90,160,.12),rgba(70,90,160,.25))}
  .signoff strong{font-size:5.5px;color:var(--ink)}
  .letterhead .doc-footer{left:20px;right:20px;bottom:9px}

  /* Folder */
  .folder{left:636px;top:80px;width:345px;height:436px}
  .folder .brand{position:absolute;right:20px;top:38px;font-size:16px}
  .folder .brand-dot{width:22px;height:22px}
  .folder .purple-art{position:absolute;left:0;right:0;top:175px;bottom:0}
  .folder .web{position:absolute;right:20px;bottom:14px;font-size:5.5px;color:#f2dff0}

  /* Business cards */
  .card-front{left:186px;top:550px;width:132px;height:75px}
  .card-front .brand{position:absolute;left:8px;top:10px;font-size:7px}
  .card-front .brand-dot{width:9px;height:9px}
  .card-front .person{position:absolute;right:10px;top:31px;text-align:right;font-size:4.6px;color:#666}
  .card-front .person strong{display:block;font-size:5.2px;color:var(--ink);font-weight:700}
  .card-front .contact{position:absolute;left:8px;right:8px;top:57px;display:flex;gap:6px;font-size:3.6px;color:#666;line-height:1.5;white-space:nowrap}
  .card-back{left:186px;top:645px;width:132px;height:75px;background:var(--plum)}
  .card-back .brand{position:absolute;left:8px;top:12px;font-size:7px;color:#fff}
  .card-back .brand-dot{width:9px;height:9px;background:#fff}
  .card-back .purple-art{position:absolute;right:0;top:0;width:34px;height:75px}
  .card-back .web{position:absolute;left:30px;bottom:8px;font-size:3.8px;color:#f2dff0}

  /* Envelopes */
  .envelope-front{left:353px;top:562px;width:328px;height:155px}
  .envelope-front .brand{position:absolute;left:22px;top:32px;font-size:11px}
  .envelope-front .brand-dot{width:16px;height:16px}
  .envelope-front .window{position:absolute;left:190px;top:88px;width:117px;height:43px;border:1px solid #d8d8d8;border-radius:4px;background:#f6f6f6}
  .envelope-front .address{position:absolute;left:58px;bottom:12px;font-size:4.4px;color:#666}
  .envelope-back{left:713px;top:562px;width:328px;height:155px}
  .envelope-back svg{position:absolute;left:0;top:0}
  .envelope-back .legal{position:absolute;left:80px;right:80px;top:128px;text-align:center;font-size:4.2px;color:#888;line-height:1.45}

  /* Small folder */
  .mini-folder{left:244px;top:775px;width:187px;height:173px}
  .mini-folder .brand{position:absolute;right:10px;top:18px;font-size:9px}
  .mini-folder .brand-dot{width:13px;height:13px}
  .mini-folder .purple-art{position:absolute;left:0;right:0;top:53px;bottom:0}
  .mini-folder .web{position:absolute;right:10px;bottom:7px;font-size:3.8px;color:#f2dff0}

  /* Disc */
  .disc{left:470px;top:777px;width:146px;height:146px;border-radius:50%}
  .disc .purple-art{position:absolute;left:0;top:0;width:30px;height:146px}
  .disc .hub{position:absolute;left:49px;top:49px;width:48px;height:48px;border-radius:50%;border:1px solid #d5d5d5;background:#f4f4f4}
  .disc .hole{position:absolute;left:63px;top:63px;width:20px;height:20px;border-radius:50%;background:var(--bg);border:1px solid #ccc}
  .disc .brand{position:absolute;left:52px;top:124px;font-size:6px}
  .disc .brand-dot{display:none}

  /* Compliments slip */
  .comp-slip{left:742px;top:772px;width:299px;height:140px}
  .comp-slip .brand{position:absolute;left:22px;top:22px;font-size:10px}
  .comp-slip .brand-dot{width:15px;height:15px}
  .comp-slip .greeting{position:absolute;left:135px;top:96px;font-size:12px;line-height:1;color:var(--plum-dark)}
  .comp-slip .greeting span{color:var(--plum)}
  .comp-slip .doc-footer{left:20px;right:14px;bottom:11px}
</style>
</head>
<body>

<!-- Letterhead -->
<section class="piece letterhead">
  <div class="brand"><span class="brand-dot"></span><span>Bright Ledger<br>Pathways</span></div>
  <div class="web">www.brightledgerpathways.example</div>
  <div class="letter-body">
    <p class="salutation">Dear sir / madame,</p>
    <p>Thank you for your interest in our training programmes. We deliver practical IT courses for medical and professional staff across the region, designed around the systems your teams use every day. Each session is led by experienced trainers and tailored to the skills, pace and schedule of your organisation. We combine classroom learning with hands-on practice so that new knowledge turns quickly into confident daily work.</p>
    <p>Our courses cover clinical records, office software, data protection and secure use of shared networks, with clear materials that staff can keep for later reference.</p>
    <p>We would be pleased to arrange a short meeting to understand your needs and propose a programme that fits your budget and timetable. Sessions can run at your premises or at our training centre, in small groups or as one-to-one coaching.</p>
    <p>Please find enclosed our current course guide. Should you have any questions, our team is happy to help by phone or email at any time. We look forward to working with you and your staff.</p>
  </div>
  <div class="signoff">
    Yours Sincerely,
    <div class="signature" role="img" aria-label="Handwritten signature"></div>
    <strong>Daniel Okoro</strong>
  </div>
  <footer class="doc-footer">
    <div class="col">P.O. Box 418263<br>Dubai UAE</div>
    <div class="col"><b>Tel.:</b> +971 4 555 0142<br><b>Fax:</b> +971 4 555 0199</div>
    <div class="col legal">Bright Ledger Pathways LLP operates as a limited liability partnership registered in England and Wales (with registered number OC702614)</div>
  </footer>
  <div class="split-bar"><span></span><span></span></div>
</section>

<!-- Presentation folder -->
<section class="piece folder">
  <div class="brand"><span class="brand-dot"></span><span>Bright Ledger<br>Pathways</span></div>
  <div class="purple-art" role="img" aria-label="Large diagonal ribbon graphic in purple tones"></div>
  <div class="web">www.brightledgerpathways.example</div>
</section>

<!-- Business card front -->
<section class="piece card-front">
  <div class="brand"><span class="brand-dot"></span><span>Bright Ledger<br>Pathways</span></div>
  <div class="person"><strong>ELENA VARGA</strong>Managing Director</div>
  <div class="contact">
    <div>P.O. Box 418263, Dubai UAE<br>Phone: +971 4 555 0142</div>
    <div>www.brightledgerpathways.example<br>info@brightledgerpathways.example</div>
  </div>
  <div class="split-bar" style="height:2px"><span></span><span></span></div>
</section>

<!-- Business card back -->
<section class="piece card-back">
  <div class="brand"><span class="brand-dot"></span><span>Bright Ledger<br>Pathways</span></div>
  <div class="purple-art" role="img" aria-label="Diagonal ribbon graphic in purple tones"></div>
  <div class="web">www.brightledgerpathways.example</div>
</section>

<!-- Envelope front -->
<section class="piece envelope-front">
  <div class="brand"><span class="brand-dot"></span><span>Bright Ledger<br>Pathways</span></div>
  <div class="window"></div>
  <div class="address">P.O. Box 418263, Dubai UAE</div>
  <div class="split-bar"><span></span><span></span></div>
</section>

<!-- Envelope back -->
<section class="piece envelope-back">
  <svg width="328" height="155" viewBox="0 0 328 155" aria-hidden="true">
    <polygon points="0,0 328,0 328,40 300,54 28,54 0,40" fill="var(--plum)"/>
  </svg>
  <div class="legal">Bright Ledger Pathways LLP operates as a limited liability partnership registered in England and Wales (with registered number OC702614)</div>
</section>

<!-- Small folder -->
<section class="piece mini-folder">
  <div class="brand"><span class="brand-dot"></span><span>Bright Ledger<br>Pathways</span></div>
  <div class="purple-art" role="img" aria-label="Diagonal ribbon graphic in purple tones"></div>
  <div class="web">www.brightledgerpathways.example</div>
</section>

<!-- Disc label -->
<section class="piece disc">
  <div class="purple-art" role="img" aria-label="Diagonal ribbon graphic in purple tones"></div>
  <div class="hub"></div>
  <div class="hole"></div>
  <div class="brand"><span class="brand-dot"></span><span>Bright Ledger<br>Pathways</span></div>
</section>

<!-- Compliments slip -->
<section class="piece comp-slip">
  <div class="brand"><span class="brand-dot"></span><span>Bright Ledger<br>Pathways</span></div>
  <div class="greeting">With <span>Compliments</span></div>
  <footer class="doc-footer">
    <div class="col">P.O. Box 418263<br>Dubai UAE</div>
    <div class="col"><b>Tel.:</b> +971 4 555 0142<br><b>Fax:</b> +971 4 555 0199</div>
    <div class="col legal">Bright Ledger Pathways LLP operates as a limited liability partnership registered in England and Wales (with registered number OC702614)</div>
  </footer>
  <div class="split-bar"><span></span><span></span></div>
</section>

</body>
</html>
```